Singapore VitaLume website

Design a SEO friendly website

Target Market(s)

Adults with health challenges

Coding

Coded - Design and coding required

Number of Pages Required

5+ page

Requirements
Must have
• Free consultation form link to email response.
Information to be taken from our respective equipment suppliers websites as per file attached.

```html
<!DOCTYPE html>
<html lang="en">
<head>
<meta charset="utf-8">
<title>Singapore VitaLume</title>
<link href="https://fonts.googleapis.com/css2?family=Open+Sans:wght@300;400;600;700&display=swap" rel="stylesheet">
<style>
:root{
  --navy:#0a1e2e;
  --navy-2:#12344a;
  --teal:#2a9bb5;
  --teal-2:#3cb8cc;
  --teal-dark:#1d6f86;
  --ink:#2b3a44;
  --muted:#7d8a93;
  --pale:#eef2f5;
  --white:#ffffff;
}
*{box-sizing:border-box;margin:0;padding:0}
html,body{width:1200px;height:4024px;overflow:hidden}
body{font-family:"Open Sans",Arial,sans-serif;color:var(--ink);background:var(--white);position:relative}
a{color:inherit;text-decoration:none}

/* header */
.site-header{position:absolute;top:0;left:0;width:1200px;height:96px;z-index:5;display:flex;align-items:center;justify-content:space-between;padding:0 60px 0 56px;border-bottom:1px solid rgba(255,255,255,.12)}
.brand{font-size:30px;font-weight:600;color:var(--white);letter-spacing:.2px}
.main-nav{display:flex;gap:38px;font-size:15px;color:#cfe2ea}
.main-nav a.active{color:var(--white);font-weight:600;border-bottom:2px solid var(--teal-2);padding-bottom:6px}

/* hero */
.hero{position:absolute;top:0;left:0;width:1200px;height:760px;background:radial-gradient(ellipse at 62% 30%,#2f7f96 0%,#163f56 35%,#0b2233 70%,#08192a 100%)}
.hero-visual{position:absolute;left:420px;top:60px;width:780px;height:560px;background:radial-gradient(ellipse at 50% 45%,rgba(140,230,240,.55) 0%,rgba(60,170,200,.35) 35%,rgba(20,70,100,0) 70%)}
.hero-copy{position:absolute;left:72px;top:230px;color:var(--white)}
.hero-copy .kicker{font-size:44px;font-weight:300;line-height:1.1}
.hero-copy h1{font-size:62px;font-weight:700;line-height:1.05}
.hero-copy p{font-size:20px;font-weight:600;color:#d6e8ef;margin-top:14px;line-height:1.35;width:460px}
.btn-outline{display:inline-block;margin-top:28px;border:2px solid var(--white);border-radius:22px;padding:9px 26px;font-size:14px;font-weight:600;color:var(--white);letter-spacing:.5px}
.hero-dots{position:absolute;right:56px;top:310px;display:flex;flex-direction:column;gap:10px}
.hero-dots span{width:8px;height:8px;border-radius:50%;background:var(--white);opacity:.6}
.hero-dots span:first-child{opacity:1}

/* pressure circles */
.pressures{position:absolute;top:590px;left:0;width:1200px;height:400px}
.pressure{position:absolute;border-radius:50%;display:flex;flex-direction:column;align-items:center;justify-content:center;text-align:center;color:var(--white);padding:0 40px}
.pressure.economic{left:118px;top:30px;width:300px;height:300px;background:radial-gradient(circle at 50% 35%,#3aa7bf,#1c6b83 75%);border:6px solid rgba(255,255,255,.9)}
.pressure.emotional{left:432px;top:0;width:340px;height:340px;background:radial-gradient(circle at 50% 35%,#24536a,#0b2536 75%);border:8px solid #1f86a1}
.pressure.brain{left:758px;top:30px;width:300px;height:300px;background:radial-gradient(circle at 50% 35%,#3aa7bf,#1c6b83 75%);border:6px solid rgba(255,255,255,.9)}
.pressure svg{width:50px;height:50px;margin-bottom:10px}
.pressure h3{font-size:21px;font-weight:600;white-space:nowrap}
.pressure p{font-size:13px;line-height:1.4;margin-top:8px;color:#e1f0f4}
.pressure .btn-outline{margin-top:14px;padding:6px 20px;font-size:11px;border-width:1.5px}

/* about */
.about{position:absolute;top:1000px;left:0;width:1200px;text-align:center}
.section-title{font-size:40px;font-weight:300;color:var(--ink);line-height:1.2}
.section-title strong{font-weight:700}
.about p{width:840px;margin:36px auto 0;font-size:16px;line-height:1.65;color:var(--muted)}
.about-visual{margin:40px auto 0;width:960px;height:180px;background:radial-gradient(ellipse at 50% 50%,rgba(29,111,134,.75) 0%,rgba(42,155,181,.5) 28%,rgba(42,155,181,.18) 55%,rgba(42,155,181,0) 75%)}

/* areas */
.areas{position:absolute;top:1600px;left:0;width:1200px;height:460px;background:var(--pale);text-align:center}
.areas .section-title{margin-top:64px;font-size:38px}
.area-cards{position:absolute;top:152px;left:98px;display:flex;gap:8px}
.area-card{position:relative;width:246px;height:246px;display:flex;flex-direction:column;justify-content:flex-end;align-items:center;padding-bottom:22px;color:var(--white);font-size:22px;font-weight:600}
.area-card.physical{background:linear-gradient(160deg,#9dc4a8,#4f8a6a 60%,#2e5a45)}
.area-card.mental{background:linear-gradient(160deg,#4fc1d2,#2a9bb5 60%,#1d7d96);justify-content:center;padding:0 30px}
.area-card.mental p{font-size:13px;font-weight:400;line-height:1.45;margin-top:12px}
.area-card.mental svg{margin-top:16px}
.area-card.emotional{background:linear-gradient(160deg,#d9d3a0,#8aa468 55%,#4f6d47)}
.area-card.brain{background:radial-gradient(circle at 50% 40%,#9a8fe0,#3b3fa0 50%,#121a4f)}

/* methods */
.methods{position:absolute;top:2100px;left:0;width:1200px;height:540px;background:linear-gradient(135deg,#c8d4da,#eef3f5)}
.methods-photo{position:absolute;right:0;top:0;width:760px;height:540px;background:linear-gradient(120deg,#dfe6ea 0%,#b9c9d2 45%,#5f7787 100%)}
.methods-panel{position:absolute;left:0;top:0;width:700px;height:540px;background:linear-gradient(150deg,#1b5e76 0%,#1e7f98 45%,#2ba6bd 100%);clip-path:polygon(0 0,78% 0,100% 50%,78% 100%,0 100%);color:var(--white);padding:104px 0 0 88px}
.methods-panel h2{font-size:38px;font-weight:300}
.methods-panel h2 strong{font-weight:700}
.methods-panel .intro{width:380px;font-size:12px;line-height:1.55;margin-top:16px;color:#d9eef3}
.method-list{display:grid;grid-template-columns:210px 210px;row-gap:24px;margin-top:40px;font-size:14px;font-weight:600;list-style:none}
.methods-panel .btn-outline{margin-top:34px}

/* how it works */
.how{position:absolute;top:2660px;left:0;width:1200px;height:480px;background:linear-gradient(180deg,#f4f6f8,#ffffff);text-align:center}
.how .section-title{margin-top:56px;font-size:38px}
.how-line{position:absolute;top:229px;height:2px;background:var(--teal)}
.how-line.first{left:332px;width:206px}
.how-line.second{left:662px;width:206px}
.steps{position:absolute;top:168px;left:140px;width:920px;display:flex;justify-content:space-between}
.step{width:260px;display:flex;flex-direction:column;align-items:center}
.step-icon{width:124px;height:124px;border-radius:50%;border:2px solid var(--teal);background:var(--white);display:flex;align-items:center;justify-content:center}
.step h3{font-size:22px;font-weight:600;margin-top:38px;color:var(--ink)}
.step p{font-size:13px;line-height:1.5;color:var(--muted);margin-top:10px}

/* consultation */
.consult{position:absolute;top:3160px;left:0;width:1200px;height:540px;background:radial-gradient(ellipse at 50% 40%,#1f5a74 0%,#0f3247 45%,#071a28 100%);text-align:center}
.consult h2{color:var(--white);font-size:38px;font-weight:300;margin-top:56px}
.consult h2 strong{font-weight:700}
.consult-form{position:absolute;left:216px;top:140px;width:768px;display:grid;grid-template-columns:1fr 1fr;gap:24px 18px}
.field{height:50px;background:var(--white);border:0;font:400 14px "Open Sans",Arial,sans-serif;padding:0 18px;text-align:left;display:flex;align-items:center;color:#556}
.field.message{grid-column:1 / 3;height:92px;align-items:flex-start;padding-top:14px}
.btn-submit{grid-column:1 / 3;justify-self:center;margin-top:10px;background:var(--teal);color:var(--white);border:0;border-radius:22px;padding:12px 34px;font:600 15px "Open Sans",Arial,sans-serif;letter-spacing:.5px}

/* footer */
.site-footer{position:absolute;top:3700px;left:0;width:1200px;height:324px;background:linear-gradient(90deg,#2a9bb5,#3bb3c4);color:var(--white)}
.footer-cols{position:absolute;top:46px;left:140px;display:flex}
.footer-about{width:360px}
.footer-about .brand{font-size:26px;font-weight:600;line-height:1.15;display:block;width:200px}
.footer-about p{font-size:11px;line-height:1.5;margin-top:14px;width:230px;color:#e6f6f9}
.socials{display:flex;gap:14px;margin-top:18px}
.socials span{width:16px;height:16px;border-radius:50%;background:var(--white);opacity:.9}
.footer-col{width:200px}
.footer-col h4{font-size:16px;font-weight:600;margin-bottom:14px}
.footer-col ul{list-style:none;font-size:11px;line-height:2;color:#e6f6f9}
.contact-list li{display:flex;align-items:center;gap:8px}
.footer-bottom{position:absolute;left:0;bottom:0;width:1200px;height:46px;background:#1d7d96;font-size:11px;display:flex;align-items:center;justify-content:center;color:#d6eef3}
</style>
</head>
<body>

<header class="site-header">
  <a class="brand" href="#">Singapore VitaLume</a>
  <nav class="main-nav">
    <a class="active" href="#">Home</a><a href="#">About Us</a><a href="#">Why Us</a><a href="#">Approach</a><a href="#">Treatment</a><a href="#">Partnership</a><a href="#">Contact</a>
  </nav>
</header>

<section class="hero">
  <div class="hero-visual" role="img" aria-label="Glowing blue illustration of a human brain with neural light trails"></div>
  <div class="hero-copy">
    <div class="kicker">Singapore</div>
    <h1>VitaLume</h1>
    <p>Providing Total Wellness for Physical, Mental, Emotional &amp; Brain Health</p>
    <a class="btn-outline" href="#">LEARN MORE</a>
  </div>
  <div class="hero-dots"><span></span><span></span><span></span></div>
</section>

<section class="pressures">
  <div class="pressure economic">
    <svg viewBox="0 0 48 48" fill="none" stroke="#fff" stroke-width="2.5"><path d="M6 40h36M12 40V26M22 40V18M32 40V22M8 20l12-10 8 6 12-10"/></svg>
    <h3>Economic Pressure</h3>
    <p>Rising costs of living and work demands weigh on everyday health.</p>
    <a class="btn-outline" href="#">LEARN MORE</a>
  </div>
  <div class="pressure emotional">
    <svg viewBox="0 0 48 48" fill="none" stroke="#fff" stroke-width="2.5"><circle cx="24" cy="24" r="18"/><path d="M16 29c4 4 12 4 16 0"/><circle cx="18" cy="20" r="1.5" fill="#fff"/><circle cx="30" cy="20" r="1.5" fill="#fff"/></svg>
    <h3>Emotional Health</h3>
    <p>Stress and anxiety affect mood, sleep and daily life balance.</p>
    <a class="btn-outline" href="#">LEARN MORE</a>
  </div>
  <div class="pressure brain">
    <svg viewBox="0 0 48 48" fill="none" stroke="#fff" stroke-width="2.5"><path d="M24 8c-6-4-16 0-15 8-5 3-5 11 0 14 0 8 9 11 15 7 6 4 15 1 15-7 5-3 5-11 0-14 1-8-9-12-15-8zM24 8v29"/></svg>
    <h3>Brain Health</h3>
    <p>Memory and focus decline can be supported with early care.</p>
    <a class="btn-outline" href="#">LEARN MORE</a>
  </div>
</section>

<section class="about">
  <h2 class="section-title">About <strong>Singapore<br>VitaLume</strong></h2>
  <p>The 21st century comes with very competitive social and economic pressures and expectations which translate to work and social stress affecting our quality of life. Most people are also living longer with improved healthcare and there will be a larger proportion.</p>
  <div class="about-visual" role="img" aria-label="Heartbeat line running through a cluster of hexagon health icons"></div>
</section>

<section class="areas">
  <h2 class="section-title">Areas of <strong>Treatment</strong></h2>
  <div class="area-cards">
    <div class="area-card physical" role="img" aria-label="Couple jogging outdoors">Physical</div>
    <div class="area-card mental">Mental
      <p>Mental strength is built through focused care and daily support.</p>
      <svg width="22" height="22" viewBox="0 0 22 22" fill="none" stroke="#fff" stroke-width="2"><path d="M11 3v16M4 12l7 7 7-7"/></svg>
    </div>
    <div class="area-card emotional" role="img" aria-label="Senior couple relaxing in a garden">Emotional</div>
    <div class="area-card brain" role="img" aria-label="Glowing digital brain illustration">Brain</div>
  </div>
</section>

<section class="methods">
  <div class="methods-photo" role="img" aria-label="Clinician guiding a patient wearing a virtual reality headset"></div>
  <div class="methods-panel">
    <h2>Methods of <strong>Treatment</strong></h2>
    <p class="intro">Our selected treatment programme is based on deep TMS, a non-invasive magnetic stimulation that opens a new era in brain care.</p>
    <ul class="method-list">
      <li>Cortiva Deep TMS</li><li>Interactive Timing</li>
      <li>Cognitive Therapy</li><li>Listening Therapy</li>
      <li>Virtual Reality</li><li>Clinical Massage</li>
    </ul>
    <a class="btn-outline" href="#">LEARN MORE</a>
  </div>
</section>

<section class="how">
  <h2 class="section-title">How does <strong>it work?</strong></h2>
  <div class="how-line first"></div>
  <div class="how-line second"></div>
  <div class="steps">
    <div class="step">
      <div class="step-icon"><svg width="56" height="56" viewBox="0 0 56 56" fill="none" stroke="#2a9bb5" stroke-width="2.5"><circle cx="24" cy="24" r="14"/><path d="M34 34l12 12"/></svg></div>
      <h3>Screening</h3>
      <p>Each client begins with simple checks that map needs and set clear goals for care.</p>
    </div>
    <div class="step">
      <div class="step-icon"><svg width="56" height="56" viewBox="0 0 56 56" fill="none" stroke="#2a9bb5" stroke-width="2.5"><rect x="8" y="12" width="40" height="28" rx="2"/><path d="M20 48h16M28 40v8"/></svg></div>
      <h3>Training</h3>
      <p>Guided sessions build strength step by step, adjusted to progress at every visit.</p>
    </div>
    <div class="step">
      <div class="step-icon"><svg width="56" height="56" viewBox="0 0 56 56" fill="none" stroke="#2a9bb5" stroke-width="2.5"><path d="M28 10c-6-4-16 0-15 8-5 3-5 11 0 14 0 8 9 11 15 7 6 4 15 1 15-7 5-3 5-11 0-14 1-8-9-12-15-8zM28 10v29"/></svg></div>
      <h3>Results</h3>
      <p>Progress is reviewed together so gains in health and focus are clear to see.</p>
    </div>
  </div>
</section>

<section class="consult" role="img" aria-label="Dark blue background with soft glowing neural light">
  <h2>Request Free <strong>Consultation</strong></h2>
  <form class="consult-form">
    <div class="field">First Name</div>
    <div class="field">Last Name</div>
    <div class="field">Email address</div>
    <div class="field">Phone Number</div>
    <div class="field message">Message</div>
    <button class="btn-submit" type="button">SUBMIT NOW</button>
  </form>
</section>

<footer class="site-footer">
  <div class="footer-cols">
    <div class="footer-about">
      <span class="brand">Singapore VitaLume</span>
      <p>Singapore VitaLume offers whole-person wellness for mind, body and brain with caring, proven programmes.</p>
      <div class="socials"><span></span><span></span><span></span><span></span></div>
    </div>
    <div class="footer-col">
      <h4>Quick Links</h4>
      <ul><li>Home</li><li>About Us</li><li>Why Us</li><li>Approach</li><li>Treatment</li></ul>
    </div>
    <div class="footer-col">
      <h4>Resources</h4>
      <ul><li>Free E-Books</li><li>Guides</li><li>News</li><li>Blog</li><li>Contact Us</li></ul>
    </div>
    <div class="footer-col">
      <h4>Contact Us</h4>
      <ul class="contact-list">
        <li><svg width="12" height="14" viewBox="0 0 12 14" fill="#fff"><path d="M6 0a5 5 0 0 0-5 5c0 4 5 9 5 9s5-5 5-9a5 5 0 0 0-5-5zm0 7a2 2 0 1 1 0-4 2 2 0 0 1 0 4z"/></svg>123 Health Avenue, Singapore 000000</li>
        <li><svg width="12" height="12" viewBox="0 0 12 12" fill="#fff"><path d="M2 0l2 3-1 2c1 2 2 3 4 4l2-1 3 2-1 2C5 12 0 7 0 1z"/></svg>+65 0000 0000</li>
        <li><svg width="12" height="10" viewBox="0 0 12 10" fill="none" stroke="#fff" stroke-width="1.3"><rect x=".7" y=".7" width="10.6" height="8.6"/><path d="M1 1l5 4 5-4"/></svg>hello@vitalume.example</li>
      </ul>
    </div>
  </div>
  <div class="footer-bottom">© 2024 Singapore VitaLume. All rights reserved.</div>
</footer>

</body>
</html>
```